Book cover for a New Adult, romance/ contemporary novel.

I need a full front, back, and spine cover for my upcoming book. The novel is a romance/ coming of age book and is similar to Every Quiet Harbor by Marissa Colfax. My main audience is women in their late teens/ early 20's. The book is an emotional, reminiscent piece and I would love to see some cover designs with a darker palette like Waiting on Belmora, Nine Rooms Between, or Bartholomew and Kip (but I also adore some lighter covers, especially those that feature the couple such as A Different Then or Past Each Hour). Feel free to send some minimal designs as well if you have any! A great idea of that would be the cover for Salt and Clover or Waiting on Belmora. If you go with a minimal design, I'd love to see silhouettes or maybe a burning candle. Another possible idea I thought of would be a scene at a concert with the crowd silhouetted and then my main character (more details on her below) standing in the middle of it all. I prefer animation/drawing etc over real models. But feel free to send me whatever you think might match the vibe, I'd love to see anything you have in mind! Some main symbols in my book are stars and candles. The main character (Marisol) is a female Korean with brown, medium length straight hair, and the love interest (Theo) is a tall and thin male Caucasian with curly brown hair. The book is openly emotional, wistful, and sets an ache in your chest, so I can't wait to see what designs you artists come up with! (My barcode will need to be included on the back cover, and I am getting that soon!)
The title is "The Weight of Daylight" and the author's name is Brenna Quill. The book's dimensions will be 5.5x8.25. The blurb for the back cover is:
When happily ever falls apart, all you can do is move forward… and reminisce. Marisol Ahn returns home from college following a tragic incident she can’t bring herself to talk about and a breakup with her boyfriend, Theo Marsh. Finding it difficult to confront her traumas, she begins therapy. Marisol takes the therapist on a rollercoaster journey of her college life, retelling the events that caused her relationship to spiral out of control and led to her dropping out of pre-med despite that being her life-long dream. Marisol sets out to remember how things were before everything got so messed up, and figure out how to continue living now that they are.
The author bio for the back cover is:
Brenna Quill is the author of The Restless and Bold. She is a self published writer from Las Vegas who likes to pretend she’s currently in a New York bookstore, drinking a latte, while listening to a carefully curated playlist. When she’s not writing, Brenna is taking care of her plant babies and cuddling with the cutest puppy in the world.

```html
<!DOCTYPE html>
<html lang="en">
<head>
<meta charset="utf-8">
<title>The Weight of Daylight — Full Cover</title>
<link rel="stylesheet" href="https://fonts.googleapis.com/css2?family=Courier+Prime:wght@400;700&display=swap">
<style>
  :root {
    --sky-storm: #4b4a50;
    --sky-dusk: #8a5a52;
    --sky-ember: #f07a4a;
    --sky-glow: #ffd25a;
    --sky-core: #fff0a0;
    --field-dark: #2b2527;
    --blurb-ink: #f8e48a;
    --bio-ink: #5a3a31;
    --title-ink: #f7c76c;
    --spine-ink: #f6e07c;
  }
  * { margin: 0; padding: 0; box-sizing: border-box; }
  html, body { width: 1200px; height: 874px; overflow: hidden; background: #222; }
  .cover {
    position: relative;
    width: 1200px;
    height: 874px;
    overflow: hidden;
    font-family: "Courier Prime", "Courier New", monospace;
  }
  .cover-art {
    position: absolute;
    inset: 0;
    background:
      linear-gradient(to bottom, transparent 0%, transparent 76%, rgba(43,37,39,0.75) 86%, var(--field-dark) 100%),
      radial-gradient(ellipse 320px 240px at 930px 450px, var(--sky-core) 0%, var(--sky-glow) 35%, rgba(255,170,70,0) 100%),
      radial-gradient(ellipse 700px 420px at 800px 460px, rgba(255,150,70,0.9) 0%, rgba(240,122,74,0) 100%),
      linear-gradient(to bottom, var(--sky-storm) 0%, var(--sky-dusk) 14%, var(--sky-ember) 38%, #f59a50 60%, #d8804a 74%, var(--field-dark) 100%);
  }
  .back-blurb {
    position: absolute;
    left: 36px;
    top: 94px;
    width: 504px;
    text-align: center;
    color: var(--blurb-ink);
    font-size: 17px;
    line-height: 20px;
    text-shadow: 0 0 2px rgba(60,30,20,0.6);
  }
  .author-bio {
    position: absolute;
    left: 50px;
    top: 448px;
    width: 466px;
    text-align: center;
    color: var(--bio-ink);
    font-size: 16.5px;
    font-weight: 700;
    line-height: 20px;
    text-transform: uppercase;
  }
  .spine-title, .spine-author {
    position: absolute;
    left: 600px;
    writing-mode: vertical-rl;
    color: var(--spine-ink);
    white-space: nowrap;
    transform: translateX(-50%);
  }
  .spine-title { top: 44px; font-size: 25px; text-transform: uppercase; }
  .spine-author { top: 648px; font-size: 28px; font-weight: 700; }
  .front-title {
    position: absolute;
    left: 632px;
    top: 30px;
    font-size: 108px;
    font-weight: 700;
    line-height: 134px;
    text-transform: uppercase;
    color: var(--title-ink);
  }
  .front-title .title-line { display: block; white-space: nowrap; }
  .front-author {
    position: absolute;
    left: 644px;
    top: 812px;
    font-size: 32px;
    font-weight: 700;
    color: var(--spine-ink);
    text-shadow: 0 0 3px rgba(40,20,10,0.7);
  }
</style>
</head>
<body>
<main class="cover">
  <div class="cover-art" role="img" aria-label="Illustration: a girl with long dark hair in a coat seen from behind, standing in a field of glowing flowers under a stormy orange and yellow sunset sky with birds"></div>

  <section class="back-blurb">
    <p>When happily ever falls apart, all you can do is move forward… and reminisce.</p>
    <p>Marisol Ahn returns home from college following a tragic incident she can’t bring herself to talk about and a breakup with her boyfriend, Theo Marsh. Finding it difficult to confront her traumas, she begins therapy.</p>
    <p>Marisol takes the therapist on a rollercoaster journey of her college life, retelling the events that caused her relationship to spiral out of control and led to her dropping out of pre-med despite that being her life-long dream.</p>
    <p>Marisol sets out to remember how things were before everything got so messed up, and figure out how to continue living now that they are.</p>
  </section>

  <section class="author-bio">
    <p>Brenna Quill is the author of The Restless and Bold.</p>
    <p>She is a self published writer from Las Vegas who likes to pretend she’s currently in a New York bookstore, drinking a latte, while listening to a carefully curated playlist.</p>
    <p>When she’s not writing, Brenna is taking care of her plant babies and cuddling with the cutest puppy in the world.</p>
  </section>

  <div class="spine-title">The Weight of Daylight</div>
  <div class="spine-author">Brenna Quill</div>

  <h1 class="front-title">
    <span class="title-line">The</span>
    <span class="title-line">Weight</span>
    <span class="title-line">Of</span>
    <span class="title-line">Daylight</span>
  </h1>
  <div class="front-author">Brenna Quill</div>
</main>
</body>
</html>
```